Design Book Cover - Win The Hiring Room

Need assistance designing a compelling cover for an eBook titled "Win The Hiring Room". eBook is a hard hitting, direct tutorial for how to succeed in a job interview. Written by Derek Pollfrey, a senior partner with 20 years interviewing people for employment at one of the largest and most prestigious consulting firms in the world.

Target Market(s)

anyone looking to land a corporate job with Summit 1000 companies

Industry/Entity Type

Consulting

```html
<!DOCTYPE html>
<html lang="en">
<head>
<meta charset="utf-8">
<title>Win The Hiring Room — Derek Pollfrey</title>
<link rel="stylesheet" href="https://fonts.googleapis.com/css2?family=Open+Sans:wght@400&family=Oswald:wght@700&display=swap">
<style>
  :root {
    --bg: #1c1c1c;
    --white: #ffffff;
    --plum: #7a1f5c;
    --sky: #3ba3c4;
    --brick: #c8323d;
    --teal: #3aa895;
    --orange: #f5821f;
    --red: #e3232b;
    --olive: #6b8e3d;
    --leaf: #6ea84a;
    --grey: #808080;
    --green: #2e9a48;
    --navy: #0e4a78;
    --rust: #a0522d;
  }
  html, body {
    margin: 0;
    padding: 0;
    width: 750px;
    height: 1200px;
    overflow: hidden;
    background: var(--bg);
  }
  .cover {
    position: relative;
    width: 750px;
    height: 1200px;
    background: var(--bg);
  }
  .cover__author {
    position: absolute;
    top: 94px;
    left: 0;
    width: 100%;
    margin: 0;
    text-align: center;
    color: var(--white);
    font-family: "Open Sans", Arial, sans-serif;
    font-weight: 400;
    font-size: 38px;
    line-height: 48px;
    letter-spacing: 1px;
  }
  .cover__title {
    position: absolute;
    left: 0;
    top: 0;
  }
  .title-line {
    font-family: "Oswald", "Arial Narrow", sans-serif;
    font-weight: 700;
  }
  .title-line--top { fill: var(--white); font-size: 182px; }
  .title-line--bottom { font-size: 126px; }
  .cover__artwork {
    position: absolute;
    left: 0;
    top: 740px;
    width: 750px;
    height: 460px;
  }
</style>
</head>
<body>
<main class="cover">
  <p class="cover__author">DEREK POLLFREY</p>

  <svg class="cover__title" width="750" height="1200" viewBox="0 0 750 1200">
    <title>Win The Hiring Room</title>
    <text class="title-line title-line--top" x="68" y="520" textLength="616" lengthAdjust="spacingAndGlyphs">WIN THE</text>
    <text class="title-line title-line--bottom" x="68" y="631" textLength="616" lengthAdjust="spacing"><tspan fill="var(--plum)">H</tspan><tspan fill="var(--sky)">I</tspan><tspan fill="var(--brick)">R</tspan><tspan fill="var(--orange)">I</tspan><tspan fill="var(--red)">N</tspan><tspan fill="var(--olive)">G</tspan> <tspan fill="var(--grey)">R</tspan><tspan fill="var(--navy)">O</tspan><tspan fill="var(--rust)">O</tspan><tspan fill="var(--teal)">M</tspan></text>
  </svg>

  <svg class="cover__artwork" width="750" height="460" viewBox="0 0 750 460" role="img" aria-label="Artwork area: rising multicoloured arrows pointing upward">
    <defs>
      <linearGradient id="artwork-hues" x1="0" y1="0" x2="1" y2="0">
        <stop offset="0" stop-color="var(--plum)"/>
        <stop offset="0.2" stop-color="var(--sky)"/>
        <stop offset="0.4" stop-color="var(--orange)"/>
        <stop offset="0.55" stop-color="var(--red)"/>
        <stop offset="0.7" stop-color="var(--green)"/>
        <stop offset="0.85" stop-color="var(--navy)"/>
        <stop offset="1" stop-color="var(--rust)"/>
      </linearGradient>
      <linearGradient id="artwork-fade" x1="0" y1="0" x2="0" y2="1">
        <stop offset="0" stop-color="var(--bg)" stop-opacity="1"/>
        <stop offset="1" stop-color="var(--bg)" stop-opacity="0.55"/>
      </linearGradient>
    </defs>
    <rect width="750" height="460" fill="url(#artwork-hues)" opacity="0.45"/>
    <rect width="750" height="460" fill="url(#artwork-fade)"/>
  </svg>
</main>
</body>
</html>
```